Stationary Design needed for luxorious bespoke tailor

We need a design for our stationary items like businescards, letters, envelope and letter head / Signature for email. Our company "VELMARDO" sells exclusively and luxourious bespoke garments and accessories for men. The desgins of letterhead, envelope and business card shoulderstand communicate luxury, high quality and good taste. We would like our logo to be used on the designs.

Target Market(s)

Gentleman with a high aproach and exclusive and luxourious suits and shirts, grooms, businesman,

Industry/Entity Type

It Company

Font styles to use
Sans Serif

Colors
ec1f27
ffffff

Requirements
Must have
• Logo, Companies name and adress, contactName internet & email, phone number line / mobile, VAT Nr. On Business Card frontpage only logo and name, adress companies on backpage. No VAT and Companies ID there. Company data; VELMARDO AG Sonnwiesweg 27 4068 Basel Switzerland VAT: CHE 472 916 503 Tax Tel 41 61 508 37 14 Mobile 41 79 842 07 91 www.velmardo.ch info@velmardo.com.
Nice to have
• -Name And phone numbers need to be able to change (for different coworkers ...)
Should not have
• no VAT in Business Card

```html
<!DOCTYPE html>
<html lang="en">
<head>
<meta charset="utf-8">
<title>VELMARDO – Business Card</title>
<link rel="stylesheet" href="https://fonts.googleapis.com/css2?family=Montserrat:wght@600&family=Questrial&display=swap">
<style>
  :root {
    --backdrop: #d4d4d4;
    --card: #29292b;
    --ink: #ffffff;
    --accent: #ec1f27;
  }
  * { margin: 0; padding: 0; box-sizing: border-box; }
  html, body {
    width: 1200px; height: 781px; overflow: hidden;
    background: var(--backdrop);
    font-family: "Questrial", "Century Gothic", sans-serif;
    color: var(--ink);
  }
  .canvas { position: relative; width: 1200px; height: 781px; }
  .card {
    position: absolute; left: 358px; width: 453px; height: 251px;
    background: var(--card);
    overflow: hidden;
  }
  .card--front { top: 103px; }
  .card--back { top: 408px; }

  .wordmark {
    position: absolute;
    font-family: "Questrial", "Century Gothic", sans-serif;
    color: var(--ink);
    letter-spacing: 0.02em;
    line-height: 1;
    white-space: nowrap;
  }
  .card--front .wordmark { left: 37px; top: 180px; font-size: 29px; }
  .card--back .wordmark { left: 39px; top: 45px; font-size: 24px; }

  .divider {
    position: absolute; left: 284px; top: 179px;
    width: 2px; height: 33px; background: var(--accent);
  }
  .person {
    position: absolute; left: 324px; top: 181px;
    max-width: 93px; white-space: nowrap;
  }
  .person__name {
    font-family: "Montserrat", sans-serif; font-weight: 600;
    font-size: 13.5px; letter-spacing: 0; line-height: 1.15;
  }
  .person__role { font-size: 12px; line-height: 1.3; }

  .contact-list {
    position: absolute; left: 40px; top: 168px; list-style: none;
    font-size: 11.5px; line-height: 14px; white-space: nowrap;
  }
  .contact-list li { display: flex; align-items: center; gap: 7px; height: 14px; }
  .contact-list svg { width: 11px; height: 11px; flex: none; }

  .address {
    position: absolute; right: 39px; top: 168px;
    font-style: normal; text-align: right;
    font-size: 11.5px; line-height: 14px; white-space: nowrap;
  }
</style>
</head>
<body>
<main class="canvas">
  <section class="card card--front" aria-label="Business card front">
    <div class="wordmark">VELMARDO</div>
    <div class="divider"></div>
    <div class="person">
      <p class="person__name">NOAH KELLER</p>
      <p class="person__role">Manager</p>
    </div>
  </section>

  <section class="card card--back" aria-label="Business card back">
    <div class="wordmark">VELMARDO</div>
    <ul class="contact-list">
      <li>
        <svg viewBox="0 0 11 11" aria-hidden="true"><rect width="11" height="11" rx="2" fill="#ec1f27"/><path d="M3 2.5l1.3 0 .6 1.6-.8.6a4 4 0 0 0 2.2 2.2l.6-.8 1.6.6v1.3c-3 .4-6-2.6-5.5-5.5z" fill="#fff"/></svg>
        <span>+41 61 508 37 14</span>
      </li>
      <li>
        <svg viewBox="0 0 11 11" aria-hidden="true"><rect width="11" height="11" rx="2" fill="#ec1f27"/><rect x="3.5" y="2" width="4" height="7" rx="0.8" fill="none" stroke="#fff" stroke-width="1"/></svg>
        <span>+41 79 842 07 91</span>
      </li>
      <li>
        <svg viewBox="0 0 11 11" aria-hidden="true"><rect width="11" height="11" rx="2" fill="#ec1f27"/><rect x="2.2" y="3.2" width="6.6" height="4.6" fill="none" stroke="#fff" stroke-width="0.9"/><path d="M2.2 3.2l3.3 2.6 3.3-2.6" fill="none" stroke="#fff" stroke-width="0.9"/></svg>
        <span>info@velmardo.com</span>
      </li>
      <li>
        <svg viewBox="0 0 11 11" aria-hidden="true"><rect width="11" height="11" rx="2" fill="#ec1f27"/><circle cx="5.5" cy="5.5" r="3.3" fill="none" stroke="#fff" stroke-width="0.8"/><ellipse cx="5.5" cy="5.5" rx="1.4" ry="3.3" fill="none" stroke="#fff" stroke-width="0.7"/><path d="M2.2 5.5h6.6" stroke="#fff" stroke-width="0.7"/></svg>
        <span>www.velmardo.ch</span>
      </li>
    </ul>
    <address class="address">
      VELMARDO AG<br>
      Sonnwiesweg 27<br>
      4068 Basel<br>
      Switzerland
    </address>
  </section>
</main>
</body>
</html>
```